CareWillow Brand Standards and Core Values

I would like to have frameable posters made up for each office using our brand standards. I would like the posters to include:Our Vision Statement:We are transforming the healthcare staffing and homecare industry with our people-oriented, world-class team. Clients choose us, and develop lasting bonds with our team because of our impeccably high standards and our reputation for always remembering this is, first and foremost, a people business. We consistently go the extra mile to ensure our nurses and those being cared for are at all times, treated with dignity and respect. We hold ourselves and those we work with to the highest possible standards. We consistently deliver what we promise, and whenever possible, even more. Our Mission Statement:We go above and beyond to ensure our clients receive the right care and the right people at the right time. Our rigorous recruitment standards result in strong caregivers who are trusted for their expertise, experience and compassion. Our Values:Through our genuine caring and compassion, we are committed to honor all with whom we interact. We are grounded in our faith and dedicated to working together as a family that consistently and passionately lives our values. Compassion Integrity and honesty Faith Decisive action Constant and never-ending improvement Personal ownership Excellence Positive attitude Passion RespectWho we are:We are friendly, servant leaders who have a sense of urgency to meet the needs of our nurses and clients. We prioritize personal relationships with genuine caring and compassion. We inspire others through our passion and energy.Our main colors are: HEX# 5C80DE, HEX# BDE080, HEX# 8C8C8Caccent colors are: HEX# 95D6E3, HEX# AD59AB, HEX# 002E57

Target Market(s)

office employee inspiration

Font styles to use
Other font styles liked:
• Verdana

Colors

Designer to choose colors to be used in the design.

Requirements
Must have
• the core values listed in description
Nice to have
• colors given in description, something fun and inspiring for office employees to help motivate them !
Should not have
• colors that are not company colors. I have listed HEX codes in description

```html
<!DOCTYPE html>
<html lang="en">
<head>
<meta charset="UTF-8">
<title>CareWillow – Our Vision</title>
<link rel="stylesheet" href="https://fonts.googleapis.com/css2?family=Open+Sans:ital,wght@0,400;0,700;0,800;1,400&display=swap">
<style>
  :root {
    --brand-blue: #5C80DE;
    --brand-green: #BDE080;
    --brand-sky: #95D6E3;
    --paper: #FFFFFF;
    --backdrop: #ECECEA;
  }
  html, body {
    margin: 0;
    padding: 0;
    width: 1200px;
    height: 1138px;
    overflow: hidden;
    background: var(--backdrop);
  }
  .poster {
    position: absolute;
    left: 202px;
    top: 19px;
    width: 795px;
    height: 1100px;
    overflow: hidden;
    background: var(--brand-blue);
    font-family: "Open Sans", Verdana, sans-serif;
    color: var(--paper);
  }
  .poster__title {
    position: absolute;
    top: 24px;
    left: 0;
    width: 100%;
    margin: 0;
    text-align: center;
    font-size: 84px;
    line-height: 100px;
    font-weight: 800;
    letter-spacing: 2px;
  }
  .poster__illustration {
    position: absolute;
    left: 73px;
    top: 195px;
    width: 650px;
    height: 458px;
  }
  .headline {
    position: absolute;
    left: 0;
    top: 692px;
    width: 100%;
    margin: 0;
    font-weight: 400;
  }
  .headline__lead {
    display: block;
    text-align: center;
    color: var(--brand-green);
    font-size: 60px;
    letter-spacing: 5px;
    line-height: 64px;
  }
  .headline__rest {
    position: absolute;
    left: 184px;
    top: 66px;
    display: block;
  }
  .headline__the {
    position: absolute;
    left: 0;
    top: 0;
    width: 78px;
    transform-origin: 0 0;
    transform: translate(0, 78px) rotate(-90deg);
    font-size: 34px;
    line-height: 34px;
    text-align: center;
  }
  .headline__healthcare {
    position: absolute;
    left: 42px;
    top: -8px;
    font-size: 56px;
    line-height: 58px;
    white-space: nowrap;
  }
  .headline__industry {
    position: absolute;
    left: 44px;
    top: 46px;
    font-size: 35px;
    line-height: 36px;
    letter-spacing: 1px;
    white-space: nowrap;
  }
  .vision-statement {
    position: absolute;
    left: 33px;
    top: 858px;
    width: 729px;
    margin: 0;
    font-size: 16.5px;
    line-height: 18.5px;
    text-align: justify;
  }
  .brand {
    position: absolute;
    left: 560px;
    top: 1014px;
    text-align: left;
  }
  .brand__name {
    display: flex;
    align-items: center;
    gap: 10px;
    font-size: 27px;
    font-weight: 700;
    line-height: 32px;
  }
  .brand__dot {
    width: 16px;
    height: 16px;
    border-radius: 50%;
    background: var(--paper);
  }
  .brand__tagline {
    margin: 4px 0 0 0;
    font-size: 14px;
    font-style: italic;
    white-space: nowrap;
  }
</style>
</head>
<body>
  <main class="poster">
    <h1 class="poster__title">OUR VISION</h1>

    <svg class="poster__illustration" viewBox="0 0 650 458" role="img" aria-label="Illustration of a green leaf butterfly hovering above two open light blue hands">
      <defs>
        <linearGradient id="illustration-fill" x1="0" y1="0" x2="0" y2="1">
          <stop offset="0" stop-color="#BDE080" stop-opacity="0.55"/>
          <stop offset="1" stop-color="#95D6E3" stop-opacity="0.55"/>
        </linearGradient>
      </defs>
      <rect width="650" height="458" rx="24" fill="url(#illustration-fill)"/>
    </svg>

    <h2 class="headline">
      <span class="headline__lead">TRANSFORMING</span>
      <span class="headline__rest">
        <span class="headline__the">THE</span>
        <span class="headline__healthcare">HEALTHCARE</span>
        <span class="headline__industry">INDUSTRY</span>
      </span>
    </h2>

    <p class="vision-statement">We are transforming the healthcare staffing and homecare industry with our people-oriented, world-class team. Clients choose us, and develop lasting bonds with our team because of our impeccably high standards and our reputation for always remembering this is, first and foremost, a people business. We consistently go the extra mile to ensure our nurses and those being cared for are at all times, treated with dignity and respect. We hold ourselves and those we work with to the highest possible standards. We consistently deliver what we promise, and whenever possible, even more.</p>

    <div class="brand">
      <div class="brand__name"><span class="brand__dot"></span>CareWillow</div>
      <div class="brand__tagline">caring for each one we serve</div>
    </div>
  </main>
</body>
</html>
```